Salon and Spa Distributor Business Card

Need a business card. We are are distributor in the salon and spa industry. We identify with natural beauty. Need a card with:
Company Name: Petal Haven"
Title: "President & CEO"
Address
Company Phone number
email
website
Tag Line:" The Professional Salon Source"

Industry/Entity Type

Business

Contact Information for Business Card

Name: Lena Morcott
Title: "President & CEO"
Address: 317 Birchfield Ln, Oakvane, NJ 07481
Company Phone number: 800-463-9152
email: lenamorcott@petalhaven-example.com
website: www.petalhaven-example.com

Requirements
Should not have
• No black backgrounds

```html
<!DOCTYPE html>
<html lang="en">
<head>
<meta charset="utf-8">
<title>Petal Haven – Business Card</title>
<link rel="stylesheet" href="https://fonts.googleapis.com/css2?family=Montserrat:wght@700&family=Questrial&display=swap">
<style>
  :root{
    --page-bg:#f1f2f1;
    --green-dark:#12753a;
    --green-light:#66bb46;
    --green-mid:#3fa742;
    --ink:#1d1d1d;
    --grey:#6b6b6b;
    --white:#ffffff;
  }
  *{box-sizing:border-box;margin:0;padding:0}
  html,body{width:1200px;height:1200px;overflow:hidden}
  body{background:var(--page-bg);font-family:"Questrial",sans-serif;position:relative}
  .card{
    position:absolute;left:160px;width:880px;height:503px;
    box-shadow:0 10px 30px rgba(0,0,0,.12);
  }
  .card--front{
    top:72px;
    background:linear-gradient(35deg,var(--green-dark) 0%,var(--green-mid) 45%,var(--green-light) 100%);
    display:flex;align-items:center;justify-content:center;gap:26px;
  }
  .front-mark{width:62px;height:62px;border-radius:50%;background:var(--white)}
  .front-name{color:var(--white);font-size:64px;letter-spacing:1px}
  .card--back{top:625px;background:var(--white)}
  .brand{position:absolute;left:40px;top:120px;width:400px;text-align:center}
  .brand-mark{width:130px;height:130px;border-radius:50%;background:linear-gradient(135deg,var(--green-light),var(--green-dark));margin:0 auto 34px}
  .brand-name{font-family:"Montserrat",sans-serif;font-weight:700;font-size:40px;color:var(--ink)}
  .brand-tagline{font-size:24px;color:var(--grey);margin-top:8px}
  .person{position:absolute;left:505px;top:88px}
  .person-name{font-family:"Montserrat",sans-serif;font-weight:700;font-size:38px;color:var(--green-mid)}
  .person-title{font-size:17px;color:var(--grey);letter-spacing:.5px;margin-top:4px}
  .divider{position:absolute;left:478px;top:292px;width:2px;height:128px;background:var(--green-mid)}
  .address{position:absolute;left:505px;top:206px;font-size:21px;color:var(--ink);line-height:1.4}
  .contacts{position:absolute;left:505px;top:300px;list-style:none}
  .contacts li{display:flex;align-items:center;gap:10px;font-size:18px;color:var(--ink);height:38px}
  .contacts svg{width:20px;height:20px;flex:none}
</style>
</head>
<body>
  <section class="card card--front">
    <span class="front-mark"></span>
    <span class="front-name">Petal Haven</span>
  </section>

  <section class="card card--back">
    <div class="brand">
      <div class="brand-mark"></div>
      <div class="brand-name">Petal Haven</div>
      <div class="brand-tagline">The Professional Salon Source</div>
    </div>

    <div class="person">
      <div class="person-name">Lena Morcott</div>
      <div class="person-title">PRESIDENT &amp; CEO</div>
    </div>

    <div class="address">317 Birchfield Ln<br>Oakvane, NJ 07481</div>

    <div class="divider"></div>

    <ul class="contacts">
      <li>
        <svg viewBox="0 0 20 20" aria-hidden="true"><circle cx="10" cy="10" r="9" fill="none" stroke="#3fa742" stroke-width="2"/><path d="M7 5.5l1.6 2.4-1 1.2a6 6 0 0 0 3.3 3.3l1.2-1 2.4 1.6-.8 1.6c-3.6.2-7.6-3.8-7.4-7.4z" fill="#3fa742"/></svg>
        800-463-9152
      </li>
      <li>
        <svg viewBox="0 0 20 20" aria-hidden="true"><rect x="1.5" y="4" width="17" height="12" fill="#3fa742"/><path d="M1.5 4l8.5 7 8.5-7" fill="none" stroke="#fff" stroke-width="1.6"/></svg>
        lenamorcott@petalhaven-example.com
      </li>
      <li>
        <svg viewBox="0 0 20 20" aria-hidden="true"><circle cx="10" cy="10" r="8.5" fill="none" stroke="#3fa742" stroke-width="2"/><ellipse cx="10" cy="10" rx="3.5" ry="8.5" fill="none" stroke="#3fa742" stroke-width="1.5"/><path d="M1.5 10h17" stroke="#3fa742" stroke-width="1.5"/></svg>
        www.petalhaven-example.com
      </li>
    </ul>
  </section>
</body>
</html>
```